Banner ad *

Replace blue banner

- An Overview / Background of the Business & Services
- We are online Wine/Spirits Merchant we ship wine throughout the USA
excluding certain states
- The Target Market / Audience you are trying to reach
- Consumers looking for online sources for hard to find wines and
vintages, our listings have detailed reviews from wine publications as long
as winery descriptions and images
- Design Specifics; any preferences or ideas for Style, Colour, Imagery,
etc
- Whichever colors will work best with wine or spirits consumers, we
have blue in our sign locally but burgundy is a rich color that is often
used with wine.

Target Market(s)

Wine drinkers ages 35-60

Industry/Entity Type

Business

Font styles to use
Serif

Colors
886aae
3176b5

Requirements
Must have
• Wine
Nice to have
• Whiskey
Should not have
• Underage people in images

```html
<!DOCTYPE html>
<html lang="en">
<head>
<meta charset="utf-8">
<title>Cellar Row Inc. – Banner</title>
<link rel="stylesheet" href="https://fonts.googleapis.com/css2?family=Fira+Sans+Condensed:ital,wght@0,700;1,300;1,700&display=swap">
<style>
  :root {
    --night: #0b0710;
    --wine-deep: #3a0a14;
    --wine-glow: #8e1426;
    --capsule-red: #b8303c;
    --capsule-dark: #2a1418;
    --cellar-blue: #1e2a6a;
    --text-white: #ffffff;
    --text-shadow: rgba(0, 0, 0, 0.85);
  }
  html, body {
    margin: 0;
    padding: 0;
    width: 1200px;
    height: 410px;
    overflow: hidden;
    background: var(--night);
  }
  .banner {
    position: relative;
    width: 1200px;
    height: 410px;
    overflow: hidden;
    font-family: "Fira Sans Condensed", "Arial Narrow", sans-serif;
    color: var(--text-white);
  }
  .cellar-photo {
    position: absolute;
    inset: 0;
    background:
      radial-gradient(ellipse 40% 70% at 72% 35%, rgba(142, 20, 38, 0.6), transparent 75%),
      radial-gradient(ellipse 30% 60% at 100% 92%, rgba(40, 60, 160, 0.65), transparent 70%),
      radial-gradient(ellipse 30% 60% at 20% 10%, rgba(40, 55, 140, 0.5), transparent 70%),
      linear-gradient(180deg, var(--wine-deep) 0%, var(--night) 100%);
  }
  .bottles-photo {
    position: absolute;
    left: 0;
    top: 0;
    width: 420px;
    height: 410px;
    background:
      linear-gradient(100deg,
        var(--night) 0%,
        var(--capsule-dark) 18%,
        #4a2a2c 30%,
        var(--capsule-dark) 36%,
        var(--capsule-red) 48%,
        #a0283a 70%,
        rgba(80, 15, 25, 0) 100%);
    -webkit-mask-image: linear-gradient(180deg, rgba(0,0,0,0.35) 0%, #000 40%, #000 100%);
    mask-image: linear-gradient(180deg, rgba(0,0,0,0.35) 0%, #000 40%, #000 100%);
  }
  .headline {
    position: absolute;
    left: 0;
    width: 1200px;
    margin: 0;
    text-align: center;
    line-height: 1;
    text-shadow: 2px 3px 4px var(--text-shadow);
  }
  .brand-name {
    top: 105px;
    font-size: 80px;
    font-weight: 700;
    font-style: italic;
    letter-spacing: 1px;
  }
  .tagline {
    top: 191px;
    font-size: 54px;
    font-weight: 300;
    font-style: italic;
  }
  .contact-email {
    top: 273px;
    font-size: 35px;
    font-weight: 700;
  }
</style>
</head>
<body>
  <div class="banner">
    <div class="cellar-photo" role="img" aria-label="Photo of a dim wine cellar rack lit in red and blue"></div>
    <div class="bottles-photo" role="img" aria-label="Photo of wine bottle necks with dark and red capsules in the foreground"></div>
    <h1 class="headline brand-name">CELLAR ROW INC.</h1>
    <p class="headline tagline">Specialists in hard to find wines and vintages</p>
    <p class="headline contact-email">hello@cellarrowinc.com</p>
  </div>
</body>
</html>
```